Marrowfield Contracting Business Cards

Front of card:

Full Logo
Name
Address
Office Phone
Cell Phone
Email
Website

Back:
Logo Mark in background
List and markets and services performed

```html
<!DOCTYPE html>
<html lang="en">
<head>
<meta charset="utf-8">
<title>Marrowfield Contracting Business Cards</title>
<link rel="stylesheet" href="https://fonts.googleapis.com/css2?family=Arimo:wght@400;700&display=swap">
<style>
  :root {
    --backdrop: #3a3a3a;
    --card: #232323;
    --card-edge: #2e2e2e;
    --red: #e0242b;
    --white: #f2f2f2;
    --grey: #8a8a8a;
    --emboss: #1b1b1b;
    --emboss-line: #2f2f2f;
  }
  * { margin: 0; padding: 0; box-sizing: border-box; }
  html, body { width: 1200px; height: 689px; overflow: hidden; }
  body {
    background: var(--backdrop);
    font-family: "Arimo", Arial, sans-serif;
    position: relative;
  }
  .card {
    position: absolute;
    top: 190px;
    width: 540px;
    height: 309px;
    background: var(--card);
    border-radius: 16px;
    border: 1px solid var(--card-edge);
    box-shadow: 0 14px 30px rgba(0,0,0,0.45);
  }
  .card-back { left: 40px; }
  .card-front { left: 620px; }

  /* back */
  .back-mark {
    position: absolute;
    left: 50%;
    top: 40px;
    transform: translateX(-50%);
    width: 150px;
    height: 150px;
    border-radius: 50%;
    border: 10px solid var(--emboss);
    box-shadow: inset 0 0 0 1px var(--emboss-line), 0 0 0 1px var(--emboss-line);
  }
  .back-name {
    position: absolute;
    top: 106px;
    left: 0; right: 0;
    text-align: center;
    font-weight: 700;
    font-size: 15px;
    letter-spacing: 1px;
    color: var(--emboss);
    text-shadow: 0 1px 0 var(--emboss-line);
    text-transform: uppercase;
  }
  .services {
    position: absolute;
    bottom: 58px;
    left: 0; right: 0;
    display: flex;
    justify-content: center;
    align-items: center;
    gap: 14px;
    font-size: 14px;
    color: var(--white);
  }
  .services .dot {
    width: 5px; height: 5px; border-radius: 50%;
    background: var(--red);
  }

  /* front */
  .brand {
    position: absolute;
    left: 34px;
    top: 78px;
    width: 220px;
    text-align: center;
  }
  .brand-circle {
    width: 86px; height: 86px;
    margin: 0 auto 14px;
    border-radius: 50%;
    border: 8px solid var(--red);
  }
  .brand-name {
    color: var(--red);
    font-weight: 700;
    font-size: 19px;
    line-height: 1.15;
    letter-spacing: 1px;
    text-transform: uppercase;
  }
  .brand-rule {
    width: 200px;
    height: 1px;
    margin: 10px auto 0;
    background: var(--grey);
  }
  .divider {
    position: absolute;
    left: 276px;
    top: 40px;
    width: 1px;
    height: 210px;
    background: linear-gradient(to bottom, transparent, var(--grey), transparent);
  }
  .contact {
    position: absolute;
    left: 300px;
    top: 62px;
    color: var(--white);
    font-size: 13px;
    line-height: 1.35;
  }
  .contact-name {
    color: var(--red);
    font-weight: 700;
    font-size: 17px;
    text-transform: uppercase;
    letter-spacing: 0.5px;
  }
  .contact-title { margin-bottom: 12px; }
  .contact-address { margin-bottom: 12px; }
  .contact-list { list-style: none; }
  .contact-list li { display: flex; align-items: center; gap: 8px; }
  .contact-list svg { width: 11px; height: 11px; fill: var(--red); flex: none; }
</style>
</head>
<body>

<section class="card card-back" aria-label="Card back">
  <div class="back-mark"></div>
  <div class="back-name">Marrowfield</div>
  <div class="services">
    <span>Dolor sit amet</span><span class="dot"></span>
    <span>Qui saepe</span><span class="dot"></span>
    <span>Accusantium</span><span class="dot"></span>
    <span>Ducimus ration</span>
  </div>
</section>

<section class="card card-front" aria-label="Card front">
  <div class="brand">
    <div class="brand-circle"></div>
    <div class="brand-name">Marrowfield<br>Contracting</div>
    <div class="brand-rule"></div>
  </div>
  <div class="divider"></div>
  <div class="contact">
    <div class="contact-name">Daniel Hargrove</div>
    <div class="contact-title">Managing Director</div>
    <div class="contact-address">1420 Alder Creek Road<br>Fairbanks, Alaska 99701</div>
    <ul class="contact-list">
      <li><svg viewBox="0 0 12 12"><path d="M2.5 0.8l2 2-1 1.4c.7 1.5 1.8 2.6 3.3 3.3l1.4-1 2 2-1.4 1.9C4.8 10.2 1.8 7.2.6 2.2z"/></svg>555-210-4471</li>
      <li><svg viewBox="0 0 12 12"><path d="M3 0h6v12H3zM4 1.5v8h4v-8z"/></svg>555-210-8836</li>
      <li><svg viewBox="0 0 12 12"><path d="M0 2h12v8H0zM1 3l5 3.5L11 3z"/></svg>info@marrowfield.com</li>
      <li><svg viewBox="0 0 12 12"><circle cx="6" cy="6" r="6"/></svg>www.marrowfield.com</li>
    </ul>
  </div>
</section>

</body>
</html>
```